Improved Business Card, Government Contracting

We are looking to update the design of our business cards. We would like to create a template that can be used for future employees and easy to update.

Halvorsen Advisory Partners, LLC is a Service Disabled Veteran Owned Small Business with headquarters located in Marlow Bend, NE. Our current website is www.hapteam.com. We have contracts in KS and VA with expansion opportunities in various other states. Our primary line of work is within government contracting and providing consulting services to various organizations within the Bureau of Frontier Works. We would like to project a professional image of our company that is consistent with the industry. Provided are previous versions of our business card template that shows our logo as well. We would like to make sure the information on the cards are easily noticeable .

Target Market(s)

Government Officials
Fellow Small Business Contractors
Large Business Contractors (ex. TRUX, Keswell Barnaby, Pryde Okonjo Whitcombe)

Industry/Entity Type

Business

Contact Information for Business Card

Dale Fenwick
Office Manager
Halvorsen Advisory Partners
Ph: 402.555.0172
Email: d.fenwick@hapteam.us
www.hapteam.com

Requirements
Must have
• The business mailing address is:
• 31842 204th Lane
• Marlow Bend, NE 66099
Nice to have
• Embossed lettering

```html
<!DOCTYPE html>
<html lang="en">
<head>
<meta charset="utf-8">
<title>Halvorsen Advisory Partners — Business Card</title>
<link rel="stylesheet" href="https://fonts.googleapis.com/css2?family=Open+Sans:wght@400;600&display=swap">
<style>
  :root {
    --navy: #262a8c;
    --navy-deep: #1e2170;
    --yellow: #ece61a;
    --white: #ffffff;
    --backdrop: #e6e7ea;
  }
  * { margin: 0; padding: 0; box-sizing: border-box; }
  html, body { width: 1200px; height: 1200px; overflow: hidden; }
  body {
    background: var(--backdrop);
    font-family: "Open Sans", Arial, sans-serif;
    position: relative;
  }
  .card {
    position: absolute;
    left: 180px;
    width: 840px;
    height: 480px;
    background: var(--navy);
    overflow: hidden;
  }
  .card-front { top: 90px; }
  .card-back { top: 630px; }

  /* Front */
  .brand-name {
    position: absolute;
    inset: 0;
    display: flex;
    flex-direction: column;
    align-items: center;
    justify-content: center;
    color: var(--white);
    font-weight: 400;
    text-transform: uppercase;
    text-align: center;
  }
  .brand-name .line-main { font-size: 64px; letter-spacing: 2px; line-height: 1.05; }
  .brand-name .line-sub { font-size: 34px; letter-spacing: 5px; line-height: 1.2; }

  /* Back */
  .contact-band {
    position: absolute;
    left: 0; right: 0; bottom: 0;
    height: 120px;
    background: var(--yellow);
  }
  .divider {
    position: absolute;
    top: 0;
    width: 4px;
    height: 360px;
    background: var(--yellow);
  }
  .divider-a { left: 168px; }
  .divider-b { left: 262px; }

  .vertical {
    position: absolute;
    bottom: 160px;
    height: 280px;
    writing-mode: vertical-rl;
    transform: rotate(180deg);
    text-align: start;
    white-space: nowrap;
  }
  .monogram {
    left: 54px;
    bottom: 130px;
    height: 200px;
    text-align: center;
    color: var(--white);
    font-size: 48px;
    font-weight: 400;
    letter-spacing: 4px;
  }
  .person { left: 188px; color: var(--white); line-height: 1.3; }
  .person-name { font-size: 26px; font-weight: 600; text-transform: uppercase; }
  .person-title { font-size: 20px; font-weight: 400; }
  .company { left: 284px; color: var(--yellow); font-size: 18px; }

  .detail { color: var(--yellow); font-size: 17px; line-height: 1.35; }
  .detail-address { left: 518px; }
  .detail-phone { left: 624px; }
  .detail-email { left: 704px; }
  .detail-web { left: 784px; }

  .contact-icons {
    position: absolute;
    left: 0; bottom: 0;
    width: 840px;
    height: 160px;
  }
</style>
</head>
<body>

  <section class="card card-front" aria-label="Business card front">
    <div class="brand-name">
      <span class="line-main">Halvorsen</span>
      <span class="line-sub">Advisory Partners</span>
    </div>
  </section>

  <section class="card card-back" aria-label="Business card back">
    <div class="contact-band"></div>
    <div class="divider divider-a"></div>
    <div class="divider divider-b"></div>

    <div class="vertical monogram">HAP</div>

    <div class="vertical person">
      <div class="person-name">Dale Fenwick</div>
      <div class="person-title">(Office Manager)</div>
    </div>

    <div class="vertical company">Halvorsen Advisory Partners</div>

    <div class="vertical detail detail-address">31842 204th Lane,<br>Marlow Bend, NE 66099</div>
    <div class="vertical detail detail-phone">402.555.0172</div>
    <div class="vertical detail detail-email">d.fenwick@hapteam.us</div>
    <div class="vertical detail detail-web">www.hapteam.com</div>

    <svg class="contact-icons" viewBox="0 0 840 160" aria-hidden="true">
      <g fill="var(--yellow)">
        <polygon points="528,42 552,12 576,42"/>
        <polygon points="612,42 636,12 660,42"/>
        <polygon points="692,42 716,12 740,42"/>
        <polygon points="772,42 796,12 820,42"/>
      </g>
      <g fill="none" stroke="var(--navy-deep)" stroke-width="4" stroke-linejoin="round" stroke-linecap="round">
        <path d="M538 98 Q552 82 566 98 Q552 114 538 98 Z"/>
        <rect x="622" y="86" width="28" height="22" rx="3"/>
        <rect x="702" y="86" width="28" height="22" rx="2"/>
        <path d="M702 88 L716 100 L730 88"/>
        <circle cx="796" cy="98" r="13"/>
        <path d="M783 98 H809 M796 85 Q788 98 796 111 M796 85 Q804 98 796 111"/>
      </g>
      <g fill="var(--navy-deep)">
        <circle cx="552" cy="98" r="4"/>
        <circle cx="644" cy="97" r="2"/>
      </g>
    </svg>
  </section>

</body>
</html>
```